Business Card Design

Business Card for professional consulting firm working with large financial institutions.

Target Market(s)

Executive buyers

Industry/Entity Type

Banking

Contact Information for Business Card

Mild creativity wanted. Not boring, but do elaborate artwork.

Font styles to use
Serif
Sans Serif

Colors

Designer to choose colors to be used in the design.

Requirements
Must have
• Standard business card features - company name, individual name, telephone, website, email, locations.
Nice to have
• Two colors
Should not have
• too many colors, fancy printing, cartoons.

```html
<!DOCTYPE html>
<html lang="en">
<head>
<meta charset="utf-8">
<title>Norvale Business Card</title>
<link rel="stylesheet" href="https://fonts.googleapis.com/css2?family=Crimson+Pro:wght@400&family=Montserrat:wght@500&family=Open+Sans:wght@400&display=swap">
<style>
  :root {
    --canvas: #1d1d1d;
    --paper: #ffffff;
    --ink: #000000;
    --accent: #ec1c24;
    --logo-grey: #6b6e72;
    --serif: "Crimson Pro", Georgia, serif;
    --sans: "Open Sans", Arial, sans-serif;
    --display: "Montserrat", Arial, sans-serif;
  }
  * { box-sizing: border-box; margin: 0; padding: 0; }
  html, body { width: 1200px; height: 900px; overflow: hidden; }
  body { background: var(--canvas); position: relative; }

  .card {
    position: absolute;
    width: 600px;
    height: 340px;
    overflow: hidden;
  }

  /* Front */
  .card--front { left: 60px; top: 90px; background: var(--paper); }
  .front__band-red-top { position: absolute; left: 0; top: 185px; width: 100%; height: 20px; background: var(--accent); }
  .front__band-black { position: absolute; left: 0; top: 205px; width: 100%; height: 22px; background: var(--ink); }
  .front__band-red-bottom { position: absolute; left: 0; top: 227px; width: 100%; height: 113px; background: var(--accent); }

  .front__brand {
    position: absolute; left: 0; top: 58px; width: 100%;
    text-align: center;
    font-family: var(--serif); font-weight: 400;
    font-size: 58px; color: var(--logo-grey);
    letter-spacing: 1px;
  }

  .front__person {
    position: absolute; left: 34px; top: 262px;
    color: var(--paper);
  }
  .person__name { font-family: var(--display); font-weight: 500; font-size: 20px; line-height: 1.2; }
  .person__role { font-family: var(--sans); font-size: 17px; line-height: 1.3; }

  .front__contact {
    position: absolute; left: 300px; top: 235px;
    width: 285px; height: 92px;
    background: var(--paper);
    padding: 8px 14px;
    display: grid;
    grid-template-columns: 58px 12px 1fr;
    font-family: var(--sans); font-size: 12.5px; line-height: 15px;
    color: var(--ink);
  }

  /* Back */
  .card--back { left: 540px; top: 470px; background: var(--ink); }
  .back__brand {
    position: absolute; left: 0; top: 92px; width: 100%;
    text-align: center;
    font-family: var(--serif); font-weight: 400;
    font-size: 64px; color: var(--paper);
    letter-spacing: 1px;
  }
  .back__web {
    position: absolute; left: 0; top: 250px; width: 100%;
    display: flex; align-items: center; gap: 12px;
    padding: 0 0 0 0;
  }
  .back__rule { flex: 1; height: 2px; background: var(--paper); }
  .back__url {
    font-family: var(--sans); font-size: 26px; color: var(--paper);
    letter-spacing: 0.5px;
  }
</style>
</head>
<body>
  <section class="card card--front" aria-label="Business card front">
    <div class="front__brand">Norvale</div>
    <div class="front__band-red-top"></div>
    <div class="front__band-black"></div>
    <div class="front__band-red-bottom"></div>
    <div class="front__person">
      <p class="person__name">Name</p>
      <p class="person__role">position</p>
    </div>
    <div class="front__contact">
      <span>Address</span><span>:</span><span>00 000 000</span>
      <span>Tel</span><span>:</span><span>00 000 000</span>
      <span>Mob</span><span>:</span><span>youremail@address</span>
      <span>E-mail</span><span>:</span><span>www.yourwebaddress</span>
      <span>Web</span><span>:</span><span></span>
    </div>
  </section>

  <section class="card card--back" aria-label="Business card back">
    <div class="back__brand">Norvale</div>
    <div class="back__web">
      <span class="back__rule"></span>
      <span class="back__url">www.website.com</span>
      <span class="back__rule"></span>
    </div>
  </section>
</body>
</html>
```